App Design for quiz app (casual gaming app)

We need an design & logo for our quiz app. Its a simple quiz app, where you pick up a category, answer three questions out of this category. After this an opponent is assigned to your game, and has to answer the same three questions. After this first round is finished, it's the opponents turn to choose a new category and answer three questions out of this category. Now it's your turn to answer the same three questions. With this done, the 2nd round is finished. One game has seven rounds.
Please find attached the balsamiq project. For all of you, do not have balsamiq, please find also the mockups as pdf.
Final delivery should be psd files
Target Market(s)
Casual Games

```html
<!DOCTYPE html>
<html lang="en">
<head>
<meta charset="utf-8">
<title>AskArena – Match Overview</title>
<link href="https://fonts.googleapis.com/css2?family=Nunito:wght@400;600;700;800&family=Varela+Round&display=swap" rel="stylesheet">
<style>
  :root {
    --green-dark: #5db874;
    --green-light: #7cc48c;
    --white: #ffffff;
    --ink: #2f3335;
    --muted: #9a9fa1;
    --soft: #b9bdbe;
    --dot-grey: #c2dfdb;
    --dot-green: #92e0a6;
    --button-bg: #e8f0ef;
    --button-border: #c9dcd8;
    --button-text: #6f8a86;
    --rule: #c8cccc;
  }
  html, body {
    margin: 0;
    padding: 0;
    width: 740px;
    height: 1200px;
    overflow: hidden;
    background: var(--white);
    font-family: "Nunito", sans-serif;
  }
  .screen {
    position: relative;
    width: 740px;
    height: 1200px;
    background: var(--white);
  }
  .app-header {
    position: absolute;
    left: 0; top: 0;
    width: 740px;
    height: 155px;
    background: var(--green-dark);
    overflow: hidden;
  }
  .app-header .header-shade {
    position: absolute;
    top: 0; left: 0;
  }
  .status-bar {
    position: absolute;
    left: 0; top: 0;
    width: 740px;
    height: 45px;
    color: var(--white);
    font-size: 21px;
    font-weight: 600;
  }
  .status-carrier { position: absolute; left: 24px; top: 10px; display: flex; align-items: center; gap: 8px; }
  .status-time { position: absolute; left: 0; right: 0; top: 10px; text-align: center; }
  .status-battery { position: absolute; right: 22px; top: 10px; display: flex; align-items: center; gap: 8px; }
  .menu-icon { position: absolute; left: 60px; top: 88px; }
  .app-title {
    position: absolute;
    left: 0; right: 0; top: 78px;
    text-align: center;
    font-family: "Varela Round", sans-serif;
    font-size: 36px;
    color: var(--white);
    letter-spacing: 0.5px;
  }
  .player {
    position: absolute;
    top: 199px;
    width: 160px;
    text-align: center;
  }
  .player-left { left: 94px; }
  .player-right { left: 490px; }
  .player-photo {
    display: block;
    width: 152px; height: 152px;
    margin: 0 auto;
  }
  .player-name {
    margin-top: 20px;
    font-size: 22px;
    color: var(--muted);
  }
  .match-timer {
    position: absolute;
    left: 0; right: 0; top: 240px;
    text-align: center;
    font-size: 50px;
    font-weight: 800;
    color: var(--ink);
  }
  .divider {
    position: absolute;
    left: 72px; top: 440px;
    width: 614px;
    border-top: 2px dashed var(--rule);
  }
  .round {
    position: absolute;
    left: 0;
    width: 740px;
    height: 70px;
  }
  .round-1 { top: 494px; }
  .round-2 { top: 621px; }
  .round-3 { top: 761px; }
  .answers {
    position: absolute;
    top: 20px;
    display: flex;
    gap: 17px;
  }
  .answers-left { left: 109px; }
  .answers-right { left: 515px; }
  .dot { width: 31px; height: 31px; border-radius: 50%; }
  .dot-missed { background: var(--dot-grey); }
  .dot-correct { background: var(--dot-green); }
  .round-info {
    position: absolute;
    left: 0; right: 0; top: 0;
    text-align: center;
  }
  .round-label { font-size: 21px; font-weight: 700; color: var(--ink); }
  .round-category { margin-top: 8px; font-size: 19px; color: var(--soft); }
  .resume-button {
    position: absolute;
    left: 133px; top: 996px;
    width: 477px; height: 62px;
    box-sizing: border-box;
    background: var(--button-bg);
    border: 2px solid var(--button-border);
    border-radius: 10px;
    color: var(--button-text);
    font-family: "Nunito", sans-serif;
    font-size: 25px;
    font-weight: 600;
    letter-spacing: 0.5px;
  }
</style>
</head>
<body>
<main class="screen">
  <header class="app-header">
    <svg class="header-shade" width="740" height="155" aria-hidden="true">
      <polygon points="378,0 740,0 740,155 428,155" fill="var(--green-light)"/>
    </svg>
    <div class="status-bar">
      <div class="status-carrier">
        <svg width="66" height="14" aria-hidden="true">
          <circle cx="7" cy="7" r="6" fill="#fff"/>
          <circle cx="20" cy="7" r="6" fill="#fff"/>
          <circle cx="33" cy="7" r="6" fill="#fff"/>
          <circle cx="46" cy="7" r="5.2" fill="none" stroke="#fff" stroke-width="1.5"/>
          <circle cx="59" cy="7" r="5.2" fill="none" stroke="#fff" stroke-width="1.5"/>
        </svg>
        <span>NOVA</span>
        <svg width="22" height="16" viewBox="0 0 22 16" aria-hidden="true">
          <path d="M2 6 A13 13 0 0 1 20 6" fill="none" stroke="#fff" stroke-width="2.4"/>
          <path d="M5.5 9.5 A8 8 0 0 1 16.5 9.5" fill="none" stroke="#fff" stroke-width="2.4"/>
          <circle cx="11" cy="13.5" r="2" fill="#fff"/>
        </svg>
      </div>
      <div class="status-time">4:21 PM</div>
      <div class="status-battery">
        <svg width="12" height="20" viewBox="0 0 12 20" aria-hidden="true">
          <path d="M1 5 L11 14 L6 18 L6 2 L11 6 L1 15" fill="none" stroke="rgba(255,255,255,0.7)" stroke-width="1.6"/>
        </svg>
        <span>100%</span>
        <svg width="50" height="20" viewBox="0 0 50 20" aria-hidden="true">
          <rect x="1" y="2" width="44" height="16" rx="3" fill="none" stroke="#fff" stroke-width="1.5"/>
          <rect x="3" y="4" width="40" height="12" rx="1.5" fill="#fff"/>
          <rect x="46" y="7" width="3" height="6" rx="1" fill="#fff"/>
        </svg>
      </div>
    </div>
    <svg class="menu-icon" width="40" height="30" aria-label="Menu" role="img">
      <rect x="0" y="0" width="40" height="3" fill="#fff"/>
      <rect x="0" y="13" width="40" height="3" fill="#fff"/>
      <rect x="0" y="26" width="40" height="3" fill="#fff"/>
    </svg>
    <h1 class="app-title" style="margin:0;font-weight:400;">AskArena</h1>
  </header>

  <section class="players">
    <div class="player player-left">
      <svg class="player-photo" viewBox="0 0 152 152" role="img" aria-label="Profile photo of Maren">
        <defs>
          <radialGradient id="photoLeft" cx="50%" cy="45%" r="60%">
            <stop offset="0%" stop-color="#e3b59c"/>
            <stop offset="100%" stop-color="#a5522e"/>
          </radialGradient>
        </defs>
        <circle cx="76" cy="76" r="76" fill="url(#photoLeft)"/>
      </svg>
      <div class="player-name">Maren</div>
    </div>
    <div class="match-timer">14:12</div>
    <div class="player player-right">
      <svg class="player-photo" viewBox="0 0 152 152" role="img" aria-label="Profile photo of Dylan">
        <defs>
          <radialGradient id="photoRight" cx="50%" cy="45%" r="60%">
            <stop offset="0%" stop-color="#c9a88f"/>
            <stop offset="100%" stop-color="#6d6963"/>
          </radialGradient>
        </defs>
        <circle cx="76" cy="76" r="76" fill="url(#photoRight)"/>
      </svg>
      <div class="player-name">Dylan</div>
    </div>
  </section>

  <div class="divider"></div>

  <section class="rounds">
    <div class="round round-1">
      <div class="answers answers-left"><span class="dot dot-missed"></span><span class="dot dot-correct"></span><span class="dot dot-correct"></span></div>
      <div class="round-info"><div class="round-label">ROUND 1</div><div class="round-category">Famous People</div></div>
      <div class="answers answers-right"><span class="dot dot-missed"></span><span class="dot dot-missed"></span><span class="dot dot-correct"></span></div>
    </div>
    <div class="round round-2">
      <div class="answers answers-left"><span class="dot dot-missed"></span><span class="dot dot-correct"></span><span class="dot dot-correct"></span></div>
      <div class="round-info"><div class="round-label">ROUND 1</div><div class="round-category">Famous People</div></div>
      <div class="answers answers-right"><span class="dot dot-missed"></span><span class="dot dot-missed"></span><span class="dot dot-correct"></span></div>
    </div>
    <div class="round round-3">
      <div class="answers answers-left"><span class="dot dot-missed"></span><span class="dot dot-correct"></span><span class="dot dot-correct"></span></div>
      <div class="round-info"><div class="round-label">ROUND 1</div><div class="round-category">Famous People</div></div>
      <div class="answers answers-right"><span class="dot dot-missed"></span><span class="dot dot-missed"></span><span class="dot dot-correct"></span></div>
    </div>
  </section>

  <button class="resume-button" type="button">RESUME</button>
</main>
</body>
</html>
```